Simple proffessional BC

I have a logo which I will attach below.
I would like the logo on the front of the card with these details in point form below:
Pre and Post Natal Yoga: Pregnancy Workshops: Hypnobirthing Courses
On the back of the card my details:
Merrin Galvey
Facebook page- calmbellieswillowharbour
Mobile- 0438 512 740

I like the idea of the card being simple, possibly just the above on a plain coloured (eggshell?) card, a card that is textured.
I am open to suggestion if it appeals!
Thank you and good luck!

Target Market(s)

Pregnant women, 20's-40's

Requirements
Must have
• Simple, compliment logo.
Make logo the feature.
Should not have

• .

```html
<!DOCTYPE html>
<html lang="en">
<head>
<meta charset="utf-8">
<title>Merrin Galvey – Business Card</title>
<link rel="stylesheet" href="https://fonts.googleapis.com/css2?family=Poiret+One&display=swap">
<style>
  :root {
    --page: #ffffff;
    --card: #eda33a;
    --band: #7f1417;
    --ink: #ffffff;
    --chip: #f0f0f2;
  }
  html, body {
    margin: 0;
    padding: 0;
    width: 1200px;
    height: 900px;
    overflow: hidden;
    background: var(--page);
  }
  .canvas {
    position: relative;
    width: 1200px;
    height: 900px;
  }
  .card {
    position: absolute;
    left: 77px;
    top: 127px;
    width: 1045px;
    height: 598px;
    border-radius: 48px;
    background: var(--card);
    overflow: hidden;
  }
  .contact-band {
    position: absolute;
    left: 0;
    top: 316px;
    width: 100%;
    height: 200px;
    background: var(--band);
  }
  .contact-band p {
    position: absolute;
    margin: 0;
    color: var(--ink);
    font-family: "Poiret One", sans-serif;
    white-space: nowrap;
    line-height: 1;
  }
  .name {
    left: 75px;
    top: 32px;
    font-size: 42px;
  }
  .phone {
    left: 74px;
    top: 88px;
    font-size: 39px;
  }
  .social {
    left: 72px;
    top: 133px;
    font-size: 34px;
  }
  .icon {
    position: absolute;
  }
  .icon-phone {
    left: 30px;
    top: 87px;
  }
  .icon-page {
    left: 28px;
    top: 141px;
    width: 31px;
    height: 31px;
    border-radius: 6px;
    background: var(--chip);
  }
</style>
</head>
<body>
  <div class="canvas">
    <div class="card">
      <div class="contact-band">
        <p class="name">Merrin Galvey</p>

        <svg class="icon icon-phone" width="24" height="38" viewBox="0 0 24 38" aria-hidden="true">
          <rect x="5" y="0" width="3" height="6" rx="1.5" fill="#ffffff"/>
          <rect x="1" y="4" width="22" height="34" rx="5" fill="#ffffff"/>
          <rect x="5" y="9" width="14" height="10" rx="1.5" fill="#7f1417"/>
          <circle cx="12" cy="29" r="2.6" fill="#7f1417"/>
        </svg>
        <p class="phone">0438 512 740</p>

        <span class="icon icon-page" aria-hidden="true"></span>
        <p class="social">calmbellieswillowharbour</p>
      </div>
    </div>
  </div>
</body>
</html>
```